Kes-Trindle web design

We need a homepage web design with final files to be provided in PSD for a company based in Brisbane called 'Kes-Trindle'. They provide innovative and reliable contract packaging solutions for local and national outsourcing buisnesses.

They have an existing website www.kes-trindle.com.au that is in dire need of an update to look more professional and sleek.

Target Market(s)

Engineers, Architects

Industry/Entity Type

Construction

Number of Pages Required

1 page

Requirements
Must have
• Main Navigation
• o Home
• o About Us
• o Spacers
• - Standard Cage Wheel Spacer
• - Heavy Duty Cage Wheel Spacer
• - Pile Cage Foot
• - PreCast Piles
• o Packaging
• o Injection Moulding
• o News
• o Contact Us
• - Client wants an updated more professional look and feel that aligns with their branding.
• - Client likes the use of displaying Products on every page eg www.gravelnook.com that has an image of the product and its name obviously looking better than this.
• The following elements are to be included in the Homepage design concept:
• - Room for a Flash banner of rotating images
• - Horizontal navigation (can you show how drop down will appear as well)
• - Logo is attached
• - Phone number needs to appear prominently on every page 07 3190 4856
• - Use Arial font throughout concept incl logo
• - Intro text on page somewhere
• - Products need to be listed on page somewhere there are 7 products (image and name with click through)
• - 2 containers/icons to highlight areas on site Latest News and Contact Us
• - Images – have attached a few that can be used in concepts and also below are some pixmarrow images that could be used in banner:
• http://www.pixmarrowfoto.com/stock-photo-4820316-several-paint-buckets.php
• http://www.pixmarrowfoto.com/stock-photo-3157840-cans-of-paint.php
• http://www.pixmarrowfoto.com/stock-photo-2748391-reinforcing-steel.php
• http://www.pixmarrowfoto.com/stock-photo-8063412-huge-bridge-pier.php
• http://www.pixmarrowfoto.com/stock-photo-1592874-highway-bridge.php
• http://www.pixmarrowfoto.com/stock-photo-4306159-bridge.php
• http://www.pixmarrowfoto.com/stock-photo-2684037-bridge-to-nowhere-yet.php

```html
<!DOCTYPE html>
<html lang="en">
<head>
<meta charset="utf-8">
<title>Kes-Trindle web design – homepage</title>
<link rel="stylesheet" href="https://fonts.googleapis.com/css2?family=Arimo:ital,wght@0,400;0,700;1,400&display=swap">
<style>
  :root {
    --board: #333333;
    --page: #ffffff;
    --navy: #2b2a6b;
    --nav: #5e5c9c;
    --nav-edge: #4a4888;
    --ink: #222222;
    --heading: #2a2a6e;
    --highlight: #ecec4c;
    --drop: rgba(58, 55, 120, 0.95);
    --grey-dark: #6b6b6b;
    --grey-a: #8b8b8b;
    --grey-b: #7d7d7d;
    --grey-light: #c9c9c9;
    --logo-red: #d8321c;
  }
  * { box-sizing: border-box; margin: 0; padding: 0; }
  html, body { width: 835px; height: 1200px; overflow: hidden; background: var(--page); }
  body { position: relative; font-family: "Arimo", Arial, sans-serif; color: var(--ink); }

  .board { position: absolute; left: 0; width: 831px; height: 543px; background: var(--board); }
  .board--default { top: 25px; }
  .board--dropdown { top: 651px; }

  .site { position: absolute; left: 84px; top: 32px; width: 668px; height: 465px; background: var(--page); }

  .banner { position: absolute; left: 0; top: 0; width: 668px; height: 157px; }
  .brand { position: absolute; left: 50px; top: 58px; display: flex; align-items: center; gap: 8px; }
  .brand__dot { width: 40px; height: 40px; border-radius: 50%; background: var(--logo-red); }
  .brand__name { font-size: 15px; font-weight: 700; color: var(--navy); }

  .nav { position: absolute; left: 0; top: 157px; width: 668px; height: 29px;
         background: linear-gradient(var(--nav), var(--nav-edge)); }
  .nav__item { position: absolute; top: 8px; font-size: 11px; color: #fff; white-space: nowrap; }
  .nav__item--active { color: var(--highlight); }
  .nav__domain { font-style: italic; }

  .dropdown { position: absolute; left: 148px; top: 186px; width: 146px; height: 84px;
              background: var(--drop); padding-top: 5px; z-index: 2; }
  .dropdown__item { font-size: 8.5px; color: var(--highlight); padding-left: 6px; height: 21px; line-height: 12px; }

  .left { position: absolute; left: 0; top: 186px; width: 167px; height: 267px; background: var(--grey-light); }
  .phone { height: 50px; background: var(--navy); display: flex; align-items: center; padding-left: 13px; gap: 9px; }
  .phone__icon { width: 32px; height: 32px; border-radius: 50%; background: #7b7aa6;
                 display: flex; align-items: center; justify-content: center; }
  .phone__number { font-size: 17px; color: #fff; }
  .feature { position: relative; height: 75px; }
  .feature--contact { background: linear-gradient(90deg, #c9b3a4 0%, #e7e2e0 45%, #d9d9dc 100%); }
  .feature--news { background: linear-gradient(90deg, #4d4a8f 0%, #6e6ea8 60%, #8a8ab6 100%); }
  .feature__label { position: absolute; font-size: 15px; }
  .feature--contact .feature__label { right: 10px; bottom: 6px; color: var(--navy); }
  .feature--news .feature__label { left: 13px; top: 17px; font-size: 19px; line-height: 18px; color: #fff; }

  .main { position: absolute; left: 167px; top: 186px; width: 334px; height: 267px; background: var(--page); padding: 12px 14px 0 14px; }
  .main__title { font-size: 20px; font-weight: 400; color: var(--heading); margin-bottom: 5px; }
  .main__text { font-size: 8.6px; line-height: 11.7px; color: var(--ink); margin-bottom: 11.7px; width: 296px; }

  .products { position: absolute; left: 501px; top: 186px; width: 167px; height: 267px; background: var(--grey-light); }
  .products__title { height: 25px; background: var(--grey-dark); color: #fff; font-size: 14px; padding: 5px 0 0 10px; font-weight: 400; }
  .product { display: flex; height: 25px; background: var(--grey-a); }
  .product:nth-child(odd) { background: var(--grey-b); }
  .product__name { flex: 1; font-size: 10.5px; color: #fff; padding: 7px 0 0 10px; }
  .product__thumb { width: 42px; height: 25px; background: linear-gradient(135deg, #f2f2f2, #5a5a5a); }

  .footer-band { position: absolute; left: 0; top: 453px; width: 668px; height: 12px; background: var(--navy); }
</style>
</head>
<body>

<!-- Homepage, default state -->
<section class="board board--default">
  <div class="site">
    <div class="banner">
      <svg width="668" height="157" viewBox="0 0 800 188" preserveAspectRatio="none">
        <defs>
          <linearGradient id="photoToneA" x1="0" x2="1" y1="0" y2="0">
            <stop offset="0" stop-color="#8b93a8"/>
            <stop offset="0.35" stop-color="#c9d3de"/>
            <stop offset="0.6" stop-color="#7ea6d6"/>
            <stop offset="1" stop-color="#9c8f80"/>
          </linearGradient>
          <linearGradient id="swooshA" x1="0" x2="1">
            <stop offset="0" stop-color="#2e2c70"/>
            <stop offset="0.5" stop-color="#8886bb"/>
            <stop offset="1" stop-color="#3a3878"/>
          </linearGradient>
        </defs>
        <path role="img" aria-label="Rotating banner photos of concrete bridge piers" d="M300,0 L800,0 L800,188 L620,188 C480,172 360,110 300,0 Z" fill="url(#photoToneA)"/>
        <path d="M78,0 L300,0 C360,110 480,172 620,188 L560,188 C340,178 150,100 78,0 Z" fill="url(#swooshA)"/>
      </svg>
      <div class="brand"><span class="brand__dot"></span><span class="brand__name">Kes-Trindle</span></div>
    </div>

    <nav class="nav">
      <span class="nav__item" style="left:24px">home</span>
      <span class="nav__item" style="left:78px">about us</span>
      <span class="nav__item" style="left:148px">spacers</span>
      <span class="nav__item" style="left:214px">packaging</span>
      <span class="nav__item" style="left:291px">injection moulding</span>
      <span class="nav__item" style="left:408px">news</span>
      <span class="nav__item" style="left:461px">contact us</span>
      <span class="nav__item nav__domain" style="left:545px">kes-trindle.com.au</span>
    </nav>

    <aside class="left">
      <div class="phone">
        <span class="phone__icon"><svg width="16" height="14" viewBox="0 0 16 14"><path d="M1,4 C1,1 15,1 15,4 L13,6 L11,4 L5,4 L3,6 Z" fill="#fff"/><rect x="3" y="7" width="10" height="6" rx="1" fill="#fff"/></svg></span>
        <span class="phone__number">07 3190 4856</span>
      </div>
      <div class="feature feature--contact" role="img" aria-label="Photo of customer service staff with headsets"><span class="feature__label">contact us</span></div>
      <div class="feature feature--news" role="img" aria-label="Photo of a businessman reading the news"><span class="feature__label">latest<br>news</span></div>
    </aside>

    <main class="main">
      <h1 class="main__title">welcome</h1>
      <p class="main__text">Lorem ipsum dolor sit amet, consectetur adipiscing elit. Fusce augue neque, porta at bibendum id, tempus nec nulla. Nam varius tincidunt pellentesque. Curabitur ut lorem eget nulla accumsan rutrum vel vitae magna. Vestibulum ante ipsum primis in faucibus orci luctus et ultrices posuere cubilia Curae; Nam vulputate nibh eu ipsum imperdiet at vehicula uma pulvinar. Etiam placerat pretium magna sed dapibus. Quisque eu lacinia nunc.</p>
      <p class="main__text">Vestibulum ante ipsum primis in faucibus orci luctus et ultrices posuere cubilia Curae; Mauris aliquam lobortis risus, et elementum quam consectetur porttitor. Maecenas laoreet rhoncus diam vitae molestie. Duis consectetur, odio sit amet congue viverra, orci felis venenatis felis, vitae rutrum turpis nibh in lorem. Pellentesque fermentum libero nisi, eu convallis leo. Fusce id aliquet elit. Nunc vel est purus, eu lacinia sapien. Quisque tempor ultrices sapien, id lacinia ipsum viverra sodales.</p>
    </main>

    <aside class="products">
      <h2 class="products__title">products:</h2>
      <div class="product-list">
        <div class="product"><span class="product__name">containers and lids</span><span class="product__thumb" role="img" aria-label="Product photo: containers and lids"></span></div>
        <div class="product"><span class="product__name">end cap</span><span class="product__thumb" role="img" aria-label="Product photo: end cap"></span></div>
        <div class="product"><span class="product__name">heavy duty wheel</span><span class="product__thumb" role="img" aria-label="Product photo: heavy duty wheel"></span></div>
        <div class="product"><span class="product__name">web wheel</span><span class="product__thumb" role="img" aria-label="Product photo: web wheel"></span></div>
        <div class="product"><span class="product__name">hinged wheel</span><span class="product__thumb" role="img" aria-label="Product photo: hinged wheel"></span></div>
        <div class="product"><span class="product__name">pile chair</span><span class="product__thumb" role="img" aria-label="Product photo: pile chair"></span></div>
        <div class="product"><span class="product__name">pipe plug</span><span class="product__thumb" role="img" aria-label="Product photo: pipe plug"></span></div>
      </div>
    </aside>

    <div class="footer-band"></div>
  </div>
</section>

<!-- Homepage, spacers dropdown open -->
<section class="board board--dropdown">
  <div class="site">
    <div class="banner">
      <svg width="668" height="157" viewBox="0 0 800 188" preserveAspectRatio="none">
        <defs>
          <linearGradient id="photoToneB" x1="0" x2="1" y1="0" y2="0">
            <stop offset="0" stop-color="#8a6a50"/>
            <stop offset="0.3" stop-color="#c9d3de"/>
            <stop offset="0.6" stop-color="#7ea6d6"/>
            <stop offset="1" stop-color="#9c8f80"/>
          </linearGradient>
          <linearGradient id="swooshB" x1="0" x2="1">
            <stop offset="0" stop-color="#2e2c70"/>
            <stop offset="0.5" stop-color="#8886bb"/>
            <stop offset="1" stop-color="#3a3878"/>
          </linearGradient>
        </defs>
        <path role="img" aria-label="Rotating banner photos of reinforcing steel and bridge piers" d="M300,0 L800,0 L800,188 L620,188 C480,172 360,110 300,0 Z" fill="url(#photoToneB)"/>
        <path d="M78,0 L300,0 C360,110 480,172 620,188 L560,188 C340,178 150,100 78,0 Z" fill="url(#swooshB)"/>
      </svg>
      <div class="brand"><span class="brand__dot"></span><span class="brand__name">Kes-Trindle</span></div>
    </div>

    <nav class="nav">
      <span class="nav__item" style="left:24px">home</span>
      <span class="nav__item" style="left:78px">about us</span>
      <span class="nav__item nav__item--active" style="left:148px">spacers</span>
      <span class="nav__item" style="left:214px">packaging</span>
      <span class="nav__item" style="left:291px">injection moulding</span>
      <span class="nav__item" style="left:408px">news</span>
      <span class="nav__item" style="left:461px">contact us</span>
      <span class="nav__item nav__domain" style="left:545px">kes-trindle.com.au</span>
    </nav>

    <ul class="dropdown">
      <li class="dropdown__item" style="list-style:none">Standard Cage Wheel Spacer</li>
      <li class="dropdown__item" style="list-style:none">Heavy Duty Cage Wheel Spacer</li>
      <li class="dropdown__item" style="list-style:none">Pile Cage Foot</li>
      <li class="dropdown__item" style="list-style:none">PreCast Piles</li>
    </ul>

    <aside class="left">
      <div class="phone">
        <span class="phone__icon"><svg width="16" height="14" viewBox="0 0 16 14"><path d="M1,4 C1,1 15,1 15,4 L13,6 L11,4 L5,4 L3,6 Z" fill="#fff"/><rect x="3" y="7" width="10" height="6" rx="1" fill="#fff"/></svg></span>
        <span class="phone__number">07 3190 4856</span>
      </div>
      <div class="feature feature--contact" role="img" aria-label="Photo of customer service staff with headsets"><span class="feature__label">contact us</span></div>
      <div class="feature feature--news" role="img" aria-label="Photo of a businessman reading the news"><span class="feature__label">latest<br>news</span></div>
    </aside>

    <main class="main">
      <h1 class="main__title">welcome</h1>
      <p class="main__text">Lorem ipsum dolor sit amet, consectetur adipiscing elit. Fusce augue neque, porta at bibendum id, tempus nec nulla. Nam varius tincidunt pellentesque. Curabitur ut lorem eget nulla accumsan rutrum vel vitae magna. Vestibulum ante ipsum primis in faucibus orci luctus et ultrices posuere cubilia Curae; Nam vulputate nibh eu ipsum imperdiet at vehicula uma pulvinar. Etiam placerat pretium magna sed dapibus. Quisque eu lacinia nunc.</p>
      <p class="main__text">Vestibulum ante ipsum primis in faucibus orci luctus et ultrices posuere cubilia Curae; Mauris aliquam lobortis risus, et elementum quam consectetur porttitor. Maecenas laoreet rhoncus diam vitae molestie. Duis consectetur, odio sit amet congue viverra, orci felis venenatis felis, vitae rutrum turpis nibh in lorem. Pellentesque fermentum libero nisi, eu convallis leo. Fusce id aliquet elit. Nunc vel est purus, eu lacinia sapien. Quisque tempor ultrices sapien, id lacinia ipsum viverra sodales.</p>
    </main>

    <aside class="products">
      <h2 class="products__title">products:</h2>
      <div class="product-list">
        <div class="product"><span class="product__name">containers and lids</span><span class="product__thumb" role="img" aria-label="Product photo: containers and lids"></span></div>
        <div class="product"><span class="product__name">end cap</span><span class="product__thumb" role="img" aria-label="Product photo: end cap"></span></div>
        <div class="product"><span class="product__name">heavy duty wheel</span><span class="product__thumb" role="img" aria-label="Product photo: heavy duty wheel"></span></div>
        <div class="product"><span class="product__name">web wheel</span><span class="product__thumb" role="img" aria-label="Product photo: web wheel"></span></div>
        <div class="product"><span class="product__name">hinged wheel</span><span class="product__thumb" role="img" aria-label="Product photo: hinged wheel"></span></div>
        <div class="product"><span class="product__name">pile chair</span><span class="product__thumb" role="img" aria-label="Product photo: pile chair"></span></div>
        <div class="product"><span class="product__name">pipe plug</span><span class="product__thumb" role="img" aria-label="Product photo: pipe plug"></span></div>
      </div>
    </aside>

    <div class="footer-band"></div>
  </div>
</section>

</body>
</html>
```